Pet Sitting Business Card

Would like a business card designed for my new pet sitting business
Card needs to match with logo design.
Blue and Orange are the theme colours.

Simple yet sophisticated design

company name:- MARIGOLD PET CARE
Dana Corbel
Owner
0472615390
dana@marigoldpetcare.com.au
www.marigoldpetcare.com.au

I'm going to close my deadline early. I will be picking a winner by the 10th of May. Please submit designs before then.
thank you

Target Market(s)

All types of professional pet lovers wishing to have their pet looked after

Industry/Entity Type

Pet

Requirements
Must have
• Logo design
Blue and orange

```html
<!DOCTYPE html>
<html lang="en">
<head>
<meta charset="utf-8">
<title>Marigold Pet Care – Business Card</title>
<link rel="stylesheet" href="https://fonts.googleapis.com/css2?family=Alegreya:ital,wght@0,400;0,700;1,400&family=Quicksand:wght@500&display=swap">
<style>
  :root {
    --brand-blue: #2094f7;
    --brand-orange: #e8842a;
    --card-white: #ffffff;
    --card-edge: #3a3a3a;
    --art-tint: #6bb8fa;
    --page: #ffffff;
  }
  * { margin: 0; padding: 0; box-sizing: border-box; }
  html, body { width: 1200px; height: 1000px; overflow: hidden; background: var(--page); }
  .canvas { position: relative; width: 1200px; height: 1000px; }
  .card {
    position: absolute; left: 313px; width: 593px; height: 340px;
    border: 1px solid var(--card-edge); overflow: hidden;
  }
  .card--front { top: 74px; background: var(--card-white); }
  .card--back { top: 460px; background: var(--brand-blue); color: var(--card-white); }

  .brand-dot {
    position: absolute; left: 266px; top: 96px; width: 62px; height: 62px;
    border-radius: 50%; background: var(--brand-orange);
  }
  .brand-name {
    position: absolute; left: 0; right: 0; top: 196px; text-align: center;
    font-family: "Alegreya", serif; font-weight: 700; font-size: 38px;
    letter-spacing: 3px; color: var(--brand-blue); line-height: 1;
  }
  .tagline {
    position: absolute; left: 0; right: 0; top: 264px; text-align: center;
    font-family: "Quicksand", sans-serif; font-weight: 500; font-size: 12.5px;
    color: var(--brand-blue); letter-spacing: 0.3px;
  }

  .contact {
    position: absolute; left: 0; right: 0; top: 56px; text-align: center;
    font-family: "Alegreya", serif; line-height: 1;
  }
  .contact__name { font-weight: 700; font-size: 21px; letter-spacing: 0.5px; }
  .contact__role { font-style: italic; font-size: 20px; margin-top: 6px; }
  .contact__phone { font-size: 16px; letter-spacing: 0.8px; margin-top: 18px; }
  .contact__email { font-size: 16px; letter-spacing: 0.4px; margin-top: 18px; }
  .contact__web { font-size: 16px; letter-spacing: 0.4px; margin-top: 5px; }

  .animal-art {
    position: absolute; left: 127px; top: 238px; width: 306px; height: 78px;
    background: var(--art-tint); border-radius: 4px;
  }
  .ground-line {
    position: absolute; left: 0; right: 0; top: 316px; height: 6px;
    background: var(--card-white);
  }
</style>
</head>
<body>
<div class="canvas">
  <section class="card card--front">
    <div class="brand-dot"></div>
    <div class="brand-name">MARIGOLD PET CARE</div>
    <div class="tagline">Caring for the pets you love most</div>
  </section>

  <section class="card card--back">
    <div class="contact">
      <div class="contact__name">Dana Corbel</div>
      <div class="contact__role">Owner</div>
      <div class="contact__phone">047.261.5390</div>
      <div class="contact__email">dana@marigoldpetcare.com.au</div>
      <div class="contact__web">www.marigoldpetcare.com.au</div>
    </div>
    <div class="animal-art" role="img" aria-label="White silhouettes of a horse, cat, rabbit, sheep and dog standing in a row"></div>
    <div class="ground-line"></div>
  </section>
</div>
</body>
</html>
```